Real Estate investment company needs billboard designs

This is our website: https://velmarkpropertygroup.com/
We are looking for some billboard concepts that uses our CEO in the design. I have attached some images and 1 billboard design that someone in our industry uses, but we don't want it exactly like his.

Industry/Entity Type

real estate

Colors

Designer to choose colors to be used in the design.

Requirements
Must have
• Company colors from websiute

```html
<!DOCTYPE html>
<html lang="en">
<head>
<meta charset="UTF-8">
<title>Velmark Property Group – Billboard</title>
<link rel="stylesheet" href="https://fonts.googleapis.com/css2?family=Oswald:wght@700&family=Montserrat:wght@600;800&display=swap">
<style>
  :root {
    --navy: #1c1a3b;
    --red: #f00f14;
    --white: #ffffff;
    --stage: #e6e9ee;
    --photo-top: #3a4360;
    --photo-bottom: #9aa6c4;
  }
  html, body {
    margin: 0;
    padding: 0;
    width: 1200px;
    height: 1200px;
    overflow: hidden;
    background: var(--stage);
  }
  .billboard {
    position: absolute;
    left: 40px;
    top: 345px;
    width: 1120px;
    height: 510px;
    background: var(--navy);
    overflow: hidden;
    font-family: "Montserrat", sans-serif;
    color: var(--white);
  }
  .brand {
    position: absolute;
    left: 42px;
    top: 34px;
    display: flex;
    align-items: center;
    gap: 12px;
  }
  .brand-mark {
    width: 22px;
    height: 22px;
    background: var(--red);
  }
  .brand-name {
    font-weight: 800;
    font-size: 24px;
    letter-spacing: 0.5px;
    text-transform: uppercase;
    color: var(--white);
    line-height: 1;
  }
  .ceo-photo {
    position: absolute;
    left: 22px;
    top: 150px;
    width: 318px;
    height: 360px;
    z-index: 2;
  }
  .headline {
    position: absolute;
    left: 372px;
    top: 80px;
    margin: 0;
    font-family: "Oswald", sans-serif;
    font-weight: 700;
    line-height: 1;
    letter-spacing: -1px;
    white-space: nowrap;
  }
  .headline-question {
    display: block;
    font-size: 90px;
  }
  .headline-offer {
    display: block;
    font-size: 64px;
    margin-top: 6px;
  }
  .headline-offer .accent { color: var(--red); }
  .cta-box {
    position: absolute;
    left: 470px;
    top: 266px;
    padding: 5px 20px;
    border: 3px solid var(--red);
    border-radius: 10px;
    font-weight: 800;
    font-size: 27px;
    letter-spacing: 0.5px;
    text-transform: uppercase;
    white-space: nowrap;
  }
  .cta-box .accent { color: var(--red); }
  .phone {
    position: absolute;
    left: 405px;
    top: 322px;
    display: flex;
    align-items: center;
    gap: 14px;
  }
  .phone-icon { width: 56px; height: 56px; }
  .phone-number {
    font-weight: 800;
    font-size: 60px;
    letter-spacing: 0.5px;
    line-height: 1;
    white-space: nowrap;
  }
  .web-band {
    position: absolute;
    left: 320px;
    right: 0;
    bottom: 0;
    height: 86px;
    background: var(--red);
    display: flex;
    align-items: center;
    justify-content: center;
    padding-left: 40px;
    box-sizing: border-box;
  }
  .web-address {
    font-weight: 600;
    font-size: 40px;
    color: var(--white);
    white-space: nowrap;
  }
</style>
</head>
<body>
  <section class="billboard">
    <div class="brand">
      <span class="brand-mark"></span>
      <span class="brand-name">Velmark Property Group</span>
    </div>

    <svg class="ceo-photo" role="img" aria-label="Photo of the company CEO in a light blue button-up shirt, pointing up toward the headline" viewBox="0 0 318 360" preserveAspectRatio="none">
      <defs>
        <linearGradient id="photoTone" x1="0" y1="0" x2="0" y2="1">
          <stop offset="0" stop-color="#3a4360"/>
          <stop offset="1" stop-color="#9aa6c4"/>
        </linearGradient>
      </defs>
      <rect width="318" height="360" fill="url(#photoTone)"/>
    </svg>

    <h1 class="headline">
      <span class="headline-question">Selling Your Home?</span>
      <span class="headline-offer">Get a Cash Offer, <span class="accent">Same Day.</span></span>
    </h1>

    <div class="cta-box">Get Your <span class="accent">Free</span> Offer</div>

    <div class="phone">
      <svg class="phone-icon" viewBox="0 0 56 56" aria-hidden="true">
        <circle cx="28" cy="28" r="28" fill="#f00f14"/>
        <path d="M20 14c1.5-1 3-.6 3.8.8l3 5c.7 1.2.4 2.6-.7 3.4l-2 1.4c1.3 3.4 3.8 6 7.2 7.4l1.5-2c.8-1.1 2.3-1.4 3.4-.7l5 3c1.3.8 1.7 2.4.8 3.8l-1.6 2.4c-1 1.5-2.9 2.2-4.6 1.7C24.6 38.8 17.2 31.4 15 20.2c-.4-1.8.3-3.6 1.8-4.6z" fill="#ffffff"/>
        <path d="M32 15a10 10 0 0 1 9 9M32 20a5 5 0 0 1 4 4" stroke="#ffffff" stroke-width="2.4" fill="none" stroke-linecap="round"/>
      </svg>
      <span class="phone-number">865-555-0142</span>
    </div>

    <div class="web-band">
      <span class="web-address">www.velmarkpropertygroup.com</span>
    </div>
  </section>
</body>
</html>
```